Flyerdesign for a Sports Homepage

I need a design for our Merchandise/Discount Flyer.
we are going to sell high class sports equipment.
the flyer should be in Size A5 or between A5 and A4.
there should be mentioned our Product names:
Product name for powerlifting: Torvik
Product name for Boxing: ZL Boxing
Product name for Martial Arts: Murelt
Product name for MMA: PitVolt
Product name for Bodybuilding: Bramfold

our Storename: PushAndDuel
Homepage: www.pushandduel.example

there should be space for entering a discount code
shop logo and brand logos: all pictures are attached.

out of the box thinking is welcome

Target Market(s)

People who do powersports like powerlifting or mma

Industry/Entity Type

Sport

Requirements
Must have
• 2 sides, all our brandnames, homepage, shop name and sports

```html
<!DOCTYPE html>
<html lang="en">
<head>
<meta charset="utf-8">
<title>PushAndDuel – Merchandise and Discount Flyer</title>
<link rel="stylesheet" href="https://fonts.googleapis.com/css2?family=Montserrat:wght@400;600;700;800&family=Roboto+Condensed:ital,wght@0,700;1,400&family=Open+Sans:wght@400&display=swap">
<style>
  :root {
    --backdrop: #c29f68;
    --sheet-top: #2f2f2f;
    --sheet-bottom: #050505;
    --gold: #b89a63;
    --gold-light: #e3cd8f;
    --ink: #111111;
    --white: #ffffff;
    --fire-deep: #2a0606;
    --fire-mid: #a3200b;
    --fire-hot: #f07a1a;
  }
  * { box-sizing: border-box; margin: 0; padding: 0; }
  html, body { width: 1200px; height: 913px; overflow: hidden; }
  body {
    background: var(--backdrop);
    position: relative;
    font-family: "Montserrat", sans-serif;
  }
  .flyer {
    position: absolute;
    top: 138px;
    width: 450px;
    height: 636px;
    background: linear-gradient(180deg, var(--sheet-top) 0%, #151515 45%, var(--sheet-bottom) 100%);
    box-shadow: 0 10px 28px rgba(0,0,0,0.35);
    overflow: hidden;
  }
  .flyer--front { left: 110px; }
  .flyer--back { left: 640px; }

  .brand-frame {
    position: absolute;
    border: 4px solid var(--gold);
    background: linear-gradient(180deg, #262626, #0d0d0d);
    display: flex;
    align-items: center;
    justify-content: center;
  }
  .flyer--front .brand-frame { left: 42px; top: 42px; width: 366px; height: 246px; }
  .flyer--back .brand-frame { left: 135px; top: 38px; width: 180px; height: 122px; border-width: 3px; }
  .brand-name {
    color: var(--gold-light);
    font-weight: 700;
    letter-spacing: 0.2em;
    white-space: nowrap;
  }
  .flyer--front .brand-name { font-size: 26px; }
  .flyer--back .brand-name { font-size: 12px; }

  .section-band {
    position: absolute;
    background: linear-gradient(90deg, #a88a55, var(--gold-light) 50%, #a88a55);
    color: var(--ink);
    text-align: center;
    letter-spacing: 0.12em;
    font-weight: 400;
  }
  .section-band strong { font-weight: 800; }
  .flyer--front .section-band { left: 42px; top: 300px; width: 366px; height: 32px; line-height: 32px; font-size: 22px; }
  .flyer--back .section-band { left: 110px; top: 180px; width: 246px; height: 32px; line-height: 32px; font-size: 21px; }

  .product {
    position: absolute;
    top: 340px;
    width: 120px;
    text-align: center;
    color: var(--white);
  }
  .flyer--back .product { top: 222px; }
  .product-art {
    width: 120px;
    height: 186px;
    background: radial-gradient(ellipse at 50% 55%, var(--fire-hot) 0%, var(--fire-mid) 35%, var(--fire-deep) 70%, #0a0a0a 100%);
  }
  .product-sport {
    margin-top: 10px;
    font-family: "Roboto Condensed", sans-serif;
    font-style: italic;
    font-size: 17px;
    line-height: 20px;
  }
  .product-name {
    font-family: "Roboto Condensed", sans-serif;
    font-weight: 700;
    font-size: 17px;
    line-height: 22px;
    text-transform: uppercase;
  }

  .discount-label {
    position: absolute;
    left: 0; width: 450px; top: 468px;
    text-align: center;
    color: var(--white);
    font-size: 17px;
    letter-spacing: 0.14em;
  }
  .discount-field {
    position: absolute;
    left: 95px; top: 494px;
    width: 330px; height: 26px;
    background: var(--white);
  }
  .coupon {
    position: absolute;
    left: 95px; top: 530px;
    width: 115px;
    text-align: center;
  }
  .coupon-amount { color: var(--gold); font-weight: 800; font-size: 28px; line-height: 30px; }
  .coupon-label { color: var(--white); font-size: 18px; letter-spacing: 0.14em; line-height: 22px; }
  .coupon-terms {
    position: absolute;
    left: 222px; top: 533px;
    width: 203px;
    color: var(--white);
    font-family: "Open Sans", sans-serif;
    font-size: 6.5px;
    line-height: 9px;
    text-align: justify;
  }

  .contact-band {
    position: absolute;
    left: 0; top: 590px;
    width: 450px; height: 32px;
  }
  .contact-band svg.band-shape { position: absolute; left: 0; top: 0; }
  .contact-line {
    position: absolute;
    left: 26px; top: 0;
    height: 32px;
    display: flex;
    align-items: center;
    gap: 6px;
    color: var(--ink);
    font-weight: 600;
    font-size: 14px;
    letter-spacing: 0.1em;
    white-space: nowrap;
  }
  .contact-line svg { flex: none; }
  .contact-line .web { font-size: 12px; letter-spacing: 0.06em; }
  .contact-line .phone { margin-right: 6px; }
</style>
</head>
<body>

<section class="flyer flyer--front" aria-label="Flyer front">
  <div class="brand-frame"><span class="brand-name">PUSH AND DUEL</span></div>
  <div class="section-band">OUR <strong>PRODUCT</strong></div>

  <div class="product" style="left:42px">
    <div class="product-art" role="img" aria-label="Torvik powerlifting brand artwork: fiery lifter with barbell"></div>
    <p class="product-sport">powerlifting:</p>
    <p class="product-name">Torvik</p>
  </div>
  <div class="product" style="left:165px">
    <div class="product-art" role="img" aria-label="ZL Boxing brand artwork: boxers in flames around a ring"></div>
    <p class="product-sport">Boxing:</p>
    <p class="product-name">ZL Boxing</p>
  </div>
  <div class="product" style="left:288px">
    <div class="product-art" role="img" aria-label="Murelt martial arts brand artwork: fighters kicking amid fire"></div>
    <p class="product-sport">Martial Arts:</p>
    <p class="product-name">Murelt</p>
  </div>

  <div class="contact-band">
    <svg class="band-shape" width="450" height="32" viewBox="0 0 450 32" aria-hidden="true">
      <rect width="450" height="32" fill="var(--gold)"/>
      <polygon points="430,0 446,0 452,32 436,32" fill="var(--white)"/>
      <polygon points="416,0 430,0 436,32 422,32" fill="#000"/>
    </svg>
    <p class="contact-line">
      <svg width="16" height="16" viewBox="0 0 24 24" aria-hidden="true"><path d="M6.6 10.8a15 15 0 0 0 6.6 6.6l2.2-2.2c.3-.3.7-.4 1-.2 1.1.4 2.3.6 3.6.6.6 0 1 .4 1 1V20c0 .6-.4 1-1 1A17 17 0 0 1 3 4c0-.6.4-1 1-1h3.5c.6 0 1 .4 1 1 0 1.3.2 2.5.6 3.6.1.3 0 .7-.2 1z" fill="none" stroke="var(--ink)" stroke-width="1.6"/></svg>
      <span class="phone">555-010-2468</span>
      <svg width="15" height="15" viewBox="0 0 24 24" aria-hidden="true"><circle cx="12" cy="12" r="10" fill="var(--ink)"/><path d="M2 12h20M12 2c3 3 3 17 0 20M12 2c-3 3-3 17 0 20" stroke="var(--gold)" stroke-width="1.4" fill="none"/></svg>
      <span class="web">PUSHANDDUEL.EXAMPLE</span>
    </p>
  </div>
</section>

<section class="flyer flyer--back" aria-label="Flyer back">
  <div class="brand-frame"><span class="brand-name">PUSH AND DUEL</span></div>
  <div class="section-band">OUR <strong>PRODUCT</strong></div>

  <div class="product" style="left:100px">
    <div class="product-art" role="img" aria-label="PitVolt MMA brand artwork: fighter above a cage in flames"></div>
    <p class="product-sport">MMA:</p>
    <p class="product-name">PitVolt</p>
  </div>
  <div class="product" style="left:230px">
    <div class="product-art" role="img" aria-label="Bramfold bodybuilding brand artwork: muscular athlete in fire"></div>
    <p class="product-sport">Bodybuilding:</p>
    <p class="product-name">Bramfold</p>
  </div>

  <p class="discount-label">DISCOUNT CODE:</p>
  <div class="discount-field" aria-label="Space for discount code"></div>

  <div class="coupon">
    <p class="coupon-amount">15 OFF</p>
    <p class="coupon-label">COUPON</p>
  </div>
  <p class="coupon-terms">Show this flyer in store or enter the code online at checkout. Valid on all five brands for one order per customer. Cannot be combined with other offers. Ask our team about sizes, stock and fitting before you buy.</p>

  <div class="contact-band">
    <svg class="band-shape" width="450" height="32" viewBox="0 0 450 32" aria-hidden="true">
      <rect width="450" height="32" fill="var(--gold)"/>
      <polygon points="430,0 446,0 452,32 436,32" fill="var(--white)"/>
      <polygon points="416,0 430,0 436,32 422,32" fill="#000"/>
    </svg>
    <p class="contact-line">
      <svg width="16" height="16" viewBox="0 0 24 24" aria-hidden="true"><path d="M6.6 10.8a15 15 0 0 0 6.6 6.6l2.2-2.2c.3-.3.7-.4 1-.2 1.1.4 2.3.6 3.6.6.6 0 1 .4 1 1V20c0 .6-.4 1-1 1A17 17 0 0 1 3 4c0-.6.4-1 1-1h3.5c.6 0 1 .4 1 1 0 1.3.2 2.5.6 3.6.1.3 0 .7-.2 1z" fill="none" stroke="var(--ink)" stroke-width="1.6"/></svg>
      <span class="phone">555-010-2468</span>
      <svg width="15" height="15" viewBox="0 0 24 24" aria-hidden="true"><circle cx="12" cy="12" r="10" fill="var(--ink)"/><path d="M2 12h20M12 2c3 3 3 17 0 20M12 2c-3 3-3 17 0 20" stroke="var(--gold)" stroke-width="1.4" fill="none"/></svg>
      <span class="web">PUSHANDDUEL.EXAMPLE</span>
    </p>
  </div>
</section>

</body>
</html>
```